Business Card Design Project

My company is called Marrow Ventures and i sell Spine implants for a company allied Kelvara and another called Pulsenet

Contact Information for Business Card

I would like something that incorporates the use of a picture of a spine as i specialize in selling spinal implants

```html
<!DOCTYPE html>
<html lang="en">
<head>
<meta charset="utf-8">
<title>Marrow Ventures – Business Card</title>
<link rel="stylesheet" href="https://fonts.googleapis.com/css2?family=Arimo:wght@400;700&display=swap">
<style>
  :root {
    --page-bg: #ffffff;
    --card-dark: #17181a;
    --card-light: #ffffff;
    --card-border: #8c8c8c;
    --brand-blue: #1e3f8f;
    --ink: #1c1a1a;
    --muted: #8a8f99;
    --divider: #a3a3a3;
    --visual-blue: #1552c2;
    --visual-blue-deep: #0b2f85;
  }
  html, body {
    margin: 0;
    padding: 0;
    width: 1200px;
    height: 1200px;
    overflow: hidden;
    background: var(--page-bg);
    font-family: "Arimo", Arial, sans-serif;
  }
  .canvas {
    position: relative;
    width: 1200px;
    height: 1200px;
  }
  .card {
    position: absolute;
    left: 180px;
    width: 838px;
    height: 479px;
    border-radius: 40px;
    overflow: hidden;
    box-sizing: border-box;
  }
  /* Front side */
  .card--front {
    top: 100px;
    background: var(--card-dark);
  }
  .feature-visual {
    position: absolute;
    left: 0;
    top: 0;
    width: 452px;
    height: 100%;
    background: linear-gradient(to right, var(--visual-blue-deep) 0%, var(--visual-blue) 45%, var(--visual-blue-deep) 80%, var(--card-dark) 100%);
  }
  .wordmark {
    position: absolute;
    text-align: center;
    font-weight: 700;
    line-height: 1;
    white-space: nowrap;
    transform: translateX(-50%);
  }
  .wordmark__main { display: block; }
  .wordmark__sub { display: block; }
  .card--front .wordmark {
    left: 616px;
    top: 194px;
    color: #ffffff;
  }
  .card--front .wordmark__main {
    font-size: 66px;
    letter-spacing: 10px;
    margin-right: -10px;
  }
  .card--front .wordmark__sub {
    font-size: 24px;
    letter-spacing: 8px;
    margin-right: -8px;
    margin-top: 14px;
  }
  /* Back side */
  .card--back {
    top: 618px;
    background: var(--card-light);
    border: 1px solid var(--card-border);
  }
  .card--back .wordmark {
    left: 218px;
    top: 203px;
    color: var(--brand-blue);
  }
  .card--back .wordmark__main {
    font-size: 54px;
    letter-spacing: 8px;
    margin-right: -8px;
  }
  .card--back .wordmark__sub {
    font-size: 19px;
    letter-spacing: 6.5px;
    margin-right: -6.5px;
    margin-top: 10px;
  }
  .divider {
    position: absolute;
    left: 395px;
    top: 91px;
    width: 2px;
    height: 297px;
    background: var(--divider);
  }
  .person {
    position: absolute;
    left: 432px;
    top: 106px;
  }
  .person__name {
    margin: 0;
    font-size: 32px;
    font-weight: 700;
    color: var(--ink);
    line-height: 1;
  }
  .person__role {
    margin: 10px 0 0;
    font-size: 22px;
    font-weight: 400;
    color: var(--muted);
    line-height: 1;
  }
  .contact-list {
    position: absolute;
    left: 432px;
    top: 208px;
    margin: 0;
    padding: 0;
    list-style: none;
  }
  .contact-list__item {
    display: flex;
    align-items: center;
    height: 34px;
    font-size: 24px;
    color: var(--ink);
    line-height: 1;
    white-space: nowrap;
  }
  .contact-list__icon {
    width: 26px;
    height: 26px;
    margin-right: 16px;
    flex: none;
    fill: var(--brand-blue);
  }
</style>
</head>
<body>
<main class="canvas">

  <section class="card card--front" aria-label="Business card front">
    <div class="feature-visual" role="img" aria-label="Illustration area: X-ray style view of a human back with the spine highlighted"></div>
    <div class="wordmark">
      <span class="wordmark__main">MARROW</span>
      <span class="wordmark__sub">VENTURES</span>
    </div>
  </section>

  <section class="card card--back" aria-label="Business card back">
    <div class="wordmark">
      <span class="wordmark__main">MARROW</span>
      <span class="wordmark__sub">VENTURES</span>
    </div>

    <div class="divider"></div>

    <div class="person">
      <h1 class="person__name">Person name</h1>
      <p class="person__role">Managing Director</p>
    </div>

    <ul class="contact-list">
      <li class="contact-list__item">
        <svg class="contact-list__icon" viewBox="0 0 26 26" aria-hidden="true">
          <path d="M2 10c0-3 5-5 11-5s11 2 11 5v2h-6v-3c-3-1-7-1-10 0v3H2z"/>
          <circle cx="13" cy="15" r="5"/>
          <circle cx="13" cy="15" r="2" fill="#fff"/>
        </svg>
        (0123) 1230-4506
      </li>
      <li class="contact-list__item">
        <svg class="contact-list__icon" viewBox="0 0 26 26" aria-hidden="true">
          <path d="M7 2h12a2 2 0 0 1 2 2v18a2 2 0 0 1-2 2H7a2 2 0 0 1-2-2V4a2 2 0 0 1 2-2zm1 3v13h10V5z"/>
          <circle cx="13" cy="21" r="1.3" fill="#fff"/>
        </svg>
        (0123) 1230-4506
      </li>
      <li class="contact-list__item">
        <svg class="contact-list__icon" viewBox="0 0 26 26" aria-hidden="true">
          <path d="M7 2h10v10H7z"/>
          <path d="M3 14h20v7H3z"/>
          <path d="M3 22h20v2H3z"/>
          <path d="M9 5h6v1H9zM9 8h6v1H9z" fill="#fff"/>
        </svg>
        (0123) 1230-4506
      </li>
      <li class="contact-list__item">
        <svg class="contact-list__icon" viewBox="0 0 26 26" aria-hidden="true">
          <path d="M2 6h22v14H2z"/>
          <path d="M3.5 7.5l9.5 7 9.5-7M3.5 18.5l7-6M22.5 18.5l-7-6" stroke="#fff" stroke-width="1.5" fill="none"/>
        </svg>
        person@marrowventures.com
      </li>
      <li class="contact-list__item">
        <svg class="contact-list__icon" viewBox="0 0 26 26" aria-hidden="true">
          <circle cx="13" cy="13" r="11"/>
          <g stroke="#fff" stroke-width="1.5" fill="none">
            <ellipse cx="13" cy="13" rx="4.5" ry="10"/>
            <path d="M2.5 13h21M4 8h18M4 18h18"/>
          </g>
        </svg>
        www.marrowventures.com
      </li>
    </ul>
  </section>

</main>
</body>
</html>
```